Brightvale Fluid Systems Corp Business Cards

Business cards to match the logo.

Company is a start up water technology company that has developed a patented system using centrifugal force to separate waste from municipal waste water to produce crystal clear clean water. Product sell starting at 2 million to governments both in the US and international.

Business cards should have a professional look with the target generally engineers.

Target Market(s)

Engineers, Government officials and investors

Industry/Entity Type

Water Treatment

Contact Information for Business Card

Business cards design will be used for 6 to 8 people with job titles. Can use the quote "If there is magic in the planet, it is contained in water." but not required to use quote. Should follow theme of Logo

Font styles to use
Other font styles liked:
• match logo font

Requirements
Nice to have
• Colors to match Logo. Business cards to match style of flow of Logo.
• Emphasis on clean look not a busy look. Clean flowing water.
Should not have
• Pictures of industrial equipment or wastewater

```html
<!DOCTYPE html>
<html lang="en">
<head>
<meta charset="utf-8">
<title>Brightvale Fluid Systems Corp Business Cards</title>
<link rel="stylesheet" href="https://fonts.googleapis.com/css2?family=Playfair+Display:wght@400&family=Tinos:wght@700&family=Open+Sans:wght@400&display=swap">
<style>
  :root {
    --backdrop: #8c8c8c;
    --card-white: #f3f3f3;
    --navy: #0e4f7e;
    --sky: #1f9ad8;
    --ink: #333333;
    --blue-top: #29aae3;
    --blue-bottom: #0a4672;
    --white: #ffffff;
  }
  * { margin: 0; padding: 0; box-sizing: border-box; }
  html, body { width: 1200px; height: 900px; overflow: hidden; }
  body { background: var(--backdrop); position: relative; }

  .card {
    position: absolute;
    top: 200px;
    width: 310px;
    height: 502px;
    box-shadow: 2px 3px 6px rgba(0,0,0,0.45);
  }
  .card--front {
    left: 308px;
    background: var(--card-white);
    border-radius: 46px 0 46px 0;
  }
  .card--back {
    left: 641px;
    background: linear-gradient(to bottom, var(--blue-top) 0%, var(--blue-bottom) 100%);
    border-radius: 0 46px 0 46px;
  }

  .wordmark {
    position: absolute;
    width: 100%;
    text-align: center;
    font-family: "Playfair Display", Georgia, serif;
    font-weight: 400;
    line-height: 1;
  }
  .wordmark__main { display: block; font-size: 23px; letter-spacing: 0.5px; }
  .wordmark__sub { display: block; font-size: 15px; letter-spacing: 6px; margin-top: 8px; padding-left: 6px; }
  .card--front .wordmark { top: 94px; left: 26px; width: 280px; color: var(--navy); }
  .card--back .wordmark { top: 382px; left: 30px; width: 260px; color: var(--white); }

  .person { position: absolute; left: 27px; top: 317px; }
  .person__name {
    font-family: "Tinos", "Times New Roman", serif;
    font-weight: 700;
    font-size: 17px;
    letter-spacing: 0.3px;
    color: var(--navy);
  }
  .person__name span { color: var(--sky); }
  .person__title {
    font-family: "Open Sans", Arial, sans-serif;
    font-size: 13px;
    color: var(--ink);
    margin-top: 1px;
  }

  .contact {
    position: absolute;
    left: 27px;
    top: 364px;
    list-style: none;
    font-family: "Open Sans", Arial, sans-serif;
    font-size: 13px;
    color: var(--ink);
    line-height: 18px;
  }
  .contact li { display: flex; align-items: center; }
  .contact svg { width: 11px; height: 11px; margin-right: 4px; fill: var(--navy); }

  .address {
    position: absolute;
    left: 27px;
    top: 428px;
    font-family: "Open Sans", Arial, sans-serif;
    font-style: normal;
    font-size: 13px;
    line-height: 19px;
    color: var(--ink);
  }
</style>
</head>
<body>
  <section class="card card--front">
    <div class="wordmark">
      <span class="wordmark__main">BRIGHTVALE FLUID</span>
      <span class="wordmark__sub">SYSTEMS</span>
    </div>

    <div class="person">
      <p class="person__name">DANIEL <span>HAYES</span></p>
      <p class="person__title">Managing Director</p>
    </div>

    <ul class="contact">
      <li>
        <svg viewBox="0 0 12 12" aria-hidden="true"><path d="M1 4.2C1 2.6 2.8 1.8 6 1.8s5 .8 5 2.4v.9H8.4V4.2H3.6v.9H1zM3.2 5.8h5.6l1.6 3.7v1.7H1.6V9.5z"/></svg>
        (044) 555018274
      </li>
      <li>
        <svg viewBox="0 0 12 12" aria-hidden="true"><path d="M3.5 0.5h5a1 1 0 0 1 1 1v9a1 1 0 0 1-1 1h-5a1 1 0 0 1-1-1v-9a1 1 0 0 1 1-1zM4 2v7h4V2zM6 9.6a.6.6 0 1 0 0 1.2a.6.6 0 1 0 0-1.2z"/></svg>
        (044)555018275
      </li>
      <li>
        <svg viewBox="0 0 12 12" aria-hidden="true"><path d="M0.8 2.5h10.4v7H0.8zM1.6 3.3v.3L6 6.5l4.4-2.9v-.3zM1.6 4.6v4.1h8.8V4.6L6 7.5z"/></svg>
        info@brightvalefluid.com
      </li>
    </ul>

    <address class="address">
      88, Harbor Lane,<br>
      Riverton, 40512
    </address>
  </section>

  <section class="card card--back">
    <div class="wordmark">
      <span class="wordmark__main">BRIGHTVALE FLUID</span>
      <span class="wordmark__sub">SYSTEMS</span>
    </div>
  </section>
</body>
</html>
```